TRV Construction and Remodeling

Prefer a matte black card with some colors that pop, but subtle. Contact info. Show General Contractor professional way. Can you please remove renovations repairs maintenance off of my logo.

Target Market(s)

Property and business investors. Homeowners

Industry/Entity Type

Construction

Contact Information for Business Card

Name: Dorian Vekkart, Title: CEO, Phone: 555-014-7392, Email: Dorian@TRVbuildNkx.example, website: www TRVbuildNkx.example

• Designer choose

Colors

Designer to choose colors to be used in the design.

Requirements
Must have
• Uniqueness. Double sided since it wont let me choose that. Professional look, be eye catching and catchy. QR code to my website
Nice to have
• Matte black background, subtle bright colors that pop, but I am open to anything. I also like black and gold with some red. Possible Harborton Ravens logo colored stars somewhere around the logo or on the back. Just to rep my city
Should not have
• pink. Something you would see somewhere else. gif pictures or generated pictures.

```html
<!DOCTYPE html>
<html lang="en">
<head>
<meta charset="utf-8">
<title>TRV Construction and Remodeling – Business Card</title>
<link href="https://fonts.googleapis.com/css2?family=Arimo:wght@400;700&family=Michroma&display=swap" rel="stylesheet">
<style>
  :root {
    --backdrop: #333333;
    --card: #1d1d1d;
    --red: #e01e25;
    --white: #ffffff;
    --soft-white: #f2f2f2;
  }
  * { margin: 0; padding: 0; box-sizing: border-box; }
  html, body {
    width: 1200px; height: 1200px; overflow: hidden;
    background: var(--backdrop);
  }
  .stage {
    position: relative; width: 1200px; height: 1200px;
    display: flex; justify-content: center; align-items: center; gap: 60px;
  }
  .card {
    width: 500px; height: 830px;
    background: var(--card);
    border-radius: 28px;
    position: relative;
    box-shadow: 0 18px 40px rgba(0,0,0,.45);
  }
  .brand {
    position: absolute; left: 0; right: 0;
    display: flex; align-items: center; justify-content: center; gap: 14px;
    font-family: "Arimo", Arial, sans-serif; font-weight: 700;
    color: var(--white);
    text-transform: uppercase; text-align: left;
    line-height: 1.05;
  }
  .brand-square { width: 22px; height: 22px; background: var(--red); flex: none; }
  .brand-name { font-size: 30px; letter-spacing: 1px; }
  .front .brand { top: 150px; }
  .back .brand { top: 370px; }
  .person {
    position: absolute; top: 395px; left: 0; right: 0; text-align: center;
  }
  .person-name {
    font-family: "Michroma", sans-serif; font-size: 28px; color: var(--red);
    font-weight: 400; letter-spacing: 1px; -webkit-text-stroke: .8px var(--red);
  }
  .person-title {
    margin-top: 8px;
    font-family: "Arimo", Arial, sans-serif; font-size: 24px; color: var(--soft-white);
  }
  .icon-row {
    position: absolute; top: 505px; left: 40px; right: 40px;
    display: flex; align-items: center; gap: 14px;
  }
  .rule { flex: 1; height: 1.5px; background: var(--red); }
  .icon {
    width: 40px; height: 40px; border-radius: 7px; background: var(--red);
    display: flex; align-items: center; justify-content: center;
  }
  .contact {
    position: absolute; top: 572px; left: 0; right: 0; text-align: center;
    font-family: "Arimo", Arial, sans-serif; font-size: 22px; line-height: 1.4;
    color: var(--soft-white);
  }
  .divider {
    position: absolute; top: 690px; left: 40px; right: 40px;
    height: 1.5px; background: var(--red);
  }
  .address {
    position: absolute; top: 708px; left: 0; right: 0; text-align: center;
    font-family: "Arimo", Arial, sans-serif; font-size: 22px; line-height: 1.4;
    color: var(--soft-white);
  }
</style>
</head>
<body>
<main class="stage">
  <section class="card front" aria-label="Card front">
    <div class="brand">
      <span class="brand-square"></span>
      <span class="brand-name">TRV Construction<br>and Remodeling</span>
    </div>
    <div class="person">
      <h1 class="person-name">DORIAN VEKKART</h1>
      <p class="person-title">CEO</p>
    </div>
    <div class="icon-row">
      <span class="rule"></span>
      <span class="icon" aria-label="Phone">
        <svg width="24" height="24" viewBox="0 0 24 24"><path fill="#fff" d="M6.6 10.8a15.2 15.2 0 0 0 6.6 6.6l2.2-2.2c.3-.3.7-.4 1-.2 1.1.4 2.3.6 3.6.6.6 0 1 .4 1 1V20c0 .6-.4 1-1 1A17 17 0 0 1 3 4c0-.6.4-1 1-1h3.5c.6 0 1 .4 1 1 0 1.3.2 2.5.6 3.6.1.3 0 .7-.2 1z"/></svg>
      </span>
      <span class="icon" aria-label="Email">
        <svg width="24" height="24" viewBox="0 0 24 24"><rect x="3" y="6" width="18" height="12" rx="1" fill="#fff"/><path d="M3.5 6.5 12 13l8.5-6.5" stroke="#e01e25" stroke-width="1.6" fill="none"/></svg>
      </span>
      <span class="icon" aria-label="Website">
        <svg width="24" height="24" viewBox="0 0 24 24"><circle cx="12" cy="12" r="8.5" fill="none" stroke="#fff" stroke-width="1.8"/><ellipse cx="12" cy="12" rx="3.6" ry="8.5" fill="none" stroke="#fff" stroke-width="1.6"/><path d="M3.5 12h17" stroke="#fff" stroke-width="1.6"/></svg>
      </span>
      <span class="rule"></span>
    </div>
    <div class="contact">
      <p>555-014-7392</p>
      <p>Dorian@TRVbuildNkx.example</p>
      <p>www.TRVbuildNkx.example</p>
    </div>
    <div class="divider"></div>
    <div class="address">
      <p>8745 Street Address Name</p>
      <p>Country Name AB 84571</p>
    </div>
  </section>
  <section class="card back" aria-label="Card back">
    <div class="brand">
      <span class="brand-square"></span>
      <span class="brand-name">TRV Construction<br>and Remodeling</span>
    </div>
  </section>
</main>
</body>
</html>
```